website for Velunora.de

In Naturheilzentrum VELUNORA, the medical team using the Advanced Laboratory examines the health status of patients and each patient is treated with special care in Germany. Multi language.
The design must show mix of modern medical service.
pages :
1. Home
2. Philosophie
3.Diagnose
4. Therapie
5. Kontakt
6.über uns
7. Zentrum ( Bilder )
8.Unser Ergebnisse
9. Anfahrt

Target Market(s)

International

Industry/Entity Type

Hospital

Font styles to use
Decorative

Colors
0455a3

Requirements
Must have
• The design must show mix of modern medical service.
• Advanced Laboratory abilities.
Nice to have
• Medical Theme
• for blue color reference see the attachment 1.jpeg

```html
<!DOCTYPE html>
<html lang="de">
<head>
<meta charset="utf-8">
<title>Velunora – Naturheilzentrum</title>
<link href="https://fonts.googleapis.com/css2?family=Cinzel:wght@400;600&family=Open+Sans:wght@400;600&display=swap" rel="stylesheet">
<style>
:root{
  --navy:#1f2c47;
  --navy-deep:#17233b;
  --blue:#0455a3;
  --blue-hero:#2f4f86;
  --red:#e3202b;
  --green:#8cc63f;
  --light:#e4e4e4;
  --white:#ffffff;
  --footer:#123454;
  --copy:#22334f;
  --text-dark:#222;
}
*{margin:0;padding:0;box-sizing:border-box}
html,body{width:1200px;height:2214px;overflow:hidden}
body{font-family:'Open Sans',Arial,sans-serif;color:var(--white);background:var(--white);position:relative}
.abs{position:absolute}
.display{font-family:'Cinzel',Georgia,serif;font-variant:small-caps;letter-spacing:1px}

/* Hero */
.hero{left:0;top:0;width:1200px;height:632px;background:radial-gradient(ellipse at 55% 45%,#4a6ea8 0%,#35568e 40%,#2a4677 100%)}
.brand{left:87px;top:34px;display:flex;align-items:center;gap:10px}
.brand-mark{width:18px;height:18px;background:var(--green)}
.brand-name{font-family:'Open Sans',Arial,sans-serif;font-weight:600;font-size:28px;color:var(--red);letter-spacing:1px}
.nav{right:86px;top:52px;display:flex;font-size:15px;text-transform:uppercase}
.nav a{color:var(--white);text-decoration:none;padding:0 12px;border-left:1px solid var(--white);line-height:16px}
.nav a:first-child{border-left:none}
.hero-title{left:0;width:1200px;top:290px;text-align:center;font-size:40px;line-height:42px;letter-spacing:5px;color:var(--white)}

/* Tiles */
.tiles{left:0;top:632px;width:1200px;height:298px;display:flex}
.tile{position:relative;width:300px;height:298px}
.tile-1{background:linear-gradient(135deg,#dfe6ef,#6b86ad 60%,#2d4e88)}
.tile-2{background:linear-gradient(135deg,#9aa7c7,#5a6ea0 50%,#2b3d73)}
.tile-3{background:linear-gradient(135deg,#cfdbe8,#7c94b7 55%,#3b5a8e)}
.tile-4{background:linear-gradient(135deg,#5f98d1,#8fb7de 50%,#c9d5e2)}
.tile-label{position:absolute;left:0;bottom:0;height:58px;padding-left:20px;font-size:22px;line-height:58px;color:var(--white);clip-path:polygon(0 0,100% 0,calc(100% - 8px) 100%,0 100%)}
.tile-label.green{background:var(--green)}
.tile-label.red{background:var(--red)}

/* Testimonials + Philosophy */
.band{left:0;top:930px;width:1200px;height:373px;background:var(--navy)}
.quote-block{left:87px;top:972px;width:480px}
.quote-head{display:flex;align-items:center;gap:10px;font-size:29px}
.quote-text{margin-top:28px;font-size:14px;line-height:24px}
.quote-author{margin-top:20px;font-size:14px;font-weight:600}
.dots{left:526px;top:1216px;display:flex;gap:4px}
.dots span{width:9px;height:9px;border-radius:50%;background:var(--white)}
.dots span.on{background:#4aa3e0}
.philosophy{left:600px;top:930px;width:600px;height:300px;background:linear-gradient(135deg,#2a4f9a 0%,#1d47a8 45%,#2a3f88 100%)}
.philosophy h2{position:absolute;left:52px;top:38px;font-size:29px;font-weight:400}
.philosophy p{position:absolute;left:52px;top:98px;width:510px;font-size:14px;line-height:24px}

/* Contact */
.help{left:0;top:1303px;width:1200px;height:521px;background:var(--light)}
.help h2{position:absolute;left:87px;top:40px;font-family:'Cinzel',Georgia,serif;font-size:29px;font-weight:400;color:var(--text-dark);letter-spacing:1px}
.field{position:absolute;left:87px;width:359px;height:34px;background:var(--white);border-radius:3px;color:#555;font-size:13px;padding:8px 15px}
.field.message{height:136px}
.agree{position:absolute;left:87px;top:396px;display:flex;align-items:center;gap:10px;font-size:12px;color:#444}
.agree .box{width:11px;height:11px;border:1px solid #888;background:var(--white);display:flex;align-items:center;justify-content:center}
.agree u{text-decoration:underline}
.submit{position:absolute;left:87px;top:433px;width:195px;height:32px;background:var(--red);color:var(--white);font-size:14px;font-weight:600;text-align:center;line-height:32px}
.video{position:absolute;left:582px;top:107px;width:532px;height:284px;background:linear-gradient(110deg,#c9cbd0 0%,#6a6c74 35%,#3a3c44 70%,#5b5457 100%)}
.video .play{position:absolute;left:237px;top:115px}
.video .bar{position:absolute;left:10px;right:10px;bottom:8px;height:22px;background:rgba(20,20,20,.6);display:flex;align-items:center;padding:0 10px;gap:14px}
.video .track{flex:1;height:4px;background:#888;position:relative}
.video .track i{position:absolute;left:0;top:0;height:4px;width:32%;background:var(--white)}

/* Footer */
.footer{left:0;top:1824px;width:1200px;height:337px;background:radial-gradient(ellipse at 45% 40%,#1d4a70 0%,#143a5c 50%,#0e2c48 100%)}
.footer h3{position:absolute;top:45px;font-size:25px;font-weight:400;color:var(--white)}
.contact-line{position:absolute;left:89px;display:flex;gap:10px;font-size:14px;line-height:21px}
.contact-line svg{flex:none;margin-top:3px}
.links{position:absolute;left:543px;top:84px;width:210px;list-style:none}
.links li{height:36px;border-bottom:1px dotted #6d88a3;font-size:14px;line-height:36px;padding-left:24px;position:relative;text-transform:uppercase}
.links li::before{content:"";position:absolute;left:2px;top:15px;width:6px;height:6px;border-radius:50%;background:var(--red)}
.social{position:absolute;left:930px;top:84px;display:flex;gap:10px}
.social span{width:16px;height:16px;border-radius:50%;background:var(--red)}
.footer .brand{position:absolute;left:930px;top:142px}
.footer .brand-name{font-size:24px}
.copyright{left:0;top:2161px;width:1200px;height:53px;background:var(--copy);font-size:14px;line-height:53px;padding-left:87px}
.copyright span{color:var(--red)}
</style>
</head>
<body>

<header class="abs hero" role="img" aria-label="Laborarzt hält ein Reagenzglas, im Hintergrund eine DNA-Helix, blau getönt">
</header>
<div class="abs brand">
  <span class="brand-mark"></span>
  <span class="brand-name">VELUNORA</span>
</div>
<nav class="abs nav">
  <a href="#">Home</a><a href="#">Philosophie</a><a href="#">Diagnose</a><a href="#">Therapie</a><a href="#">Kontakt</a><a href="#">Über uns</a><a href="#">Zentrum</a>
</nav>
<h1 class="abs hero-title display">Ein Professionelles<br>Medizinisches Team</h1>

<section class="abs tiles">
  <div class="tile tile-1" role="img" aria-label="Laborantin am Mikroskop"><span class="tile-label green" style="width:260px">Spezialbehandlung</span></div>
  <div class="tile tile-2" role="img" aria-label="Ultraschall-Diagnosegerät mit Bildschirm"><span class="tile-label red" style="width:235px">Diagnose</span></div>
  <div class="tile tile-3" role="img" aria-label="Arzt untersucht Proben am Mikroskop im Labor"><span class="tile-label green" style="width:235px">Unsere Ergebnisse</span></div>
  <div class="tile tile-4" role="img" aria-label="Physiotherapeut behandelt das Bein eines Patienten"><span class="tile-label red" style="width:235px">Therapie</span></div>
</section>

<section class="abs band"></section>
<div class="abs quote-block">
  <div class="quote-head">
    <svg width="46" height="40" viewBox="0 0 46 40"><path d="M0 40V22C0 9 7 2 18 0l2 5C13 8 10 13 10 18h9v22zM26 40V22C26 9 33 2 44 0l2 5c-7 3-10 8-10 13h9v22z" fill="#fff"/></svg>
    <h2 class="display" style="font-weight:400;font-size:29px">Referenzen</h2>
  </div>
  <p class="quote-text">“Lorem Ipsum is simply dummy text of the printing and typesetting industry. Lorem Ipsum has been the industry's standard dummy text ever since the 1500s, when an unknown printer took a galley of type and scrambled it to make a type specimen book.”</p>
  <p class="quote-author">~ Name Here</p>
</div>
<div class="abs dots"><span></span><span></span><span class="on"></span><span></span></div>

<section class="abs philosophy" role="img" aria-label="Blaues Polygonmuster als Hintergrund">
  <h2 class="display">Philosophie</h2>
  <p>Lorem Ipsum is simply dummy text of the printing and typesetting industry. Lorem Ipsum has been the industry's standard dummy text ever since the 1500s, when an unknown printer took a galley of type and scrambled it to make a type specimen book.<br>It has survived not only five centuries, but also the leap into electronic typesetting, remaining essentially unchanged. It was popularised in the 1960s with the release of Letraset sheets containing Lorem Ipsum.</p>
</section>

<section class="abs help">
  <h2>HOW CAN WE HELP YOU?</h2>
  <div class="field" style="top:107px">Name</div>
  <div class="field" style="top:151px">Phone Number</div>
  <div class="field" style="top:195px">Email</div>
  <div class="field message" style="top:239px">Message</div>
  <div class="agree"><span class="box"><svg width="9" height="9" viewBox="0 0 9 9"><path d="M1 5l2 2 5-6" stroke="#334" stroke-width="1.5" fill="none"/></svg></span>I agree to Kelvara <u>Terms of Services</u></div>
  <div class="submit">EVALUATE MY CASE</div>
  <div class="video" role="img" aria-label="Videostandbild: Ärztin mit Stethoskop hält ein Klemmbrett">
    <svg class="play" width="56" height="56" viewBox="0 0 56 56"><circle cx="28" cy="28" r="25" stroke="#fff" stroke-width="4" fill="none"/><path d="M22 16l17 12-17 12z" fill="#fff"/></svg>
    <div class="bar">
      <svg width="10" height="12" viewBox="0 0 10 12"><path d="M0 0l10 6-10 6z" fill="#fff"/></svg>
      <div class="track"><i></i></div>
      <svg width="36" height="10" viewBox="0 0 36 10"><rect x="0" y="2" width="20" height="6" fill="#fff"/><rect x="26" y="1" width="8" height="8" fill="none" stroke="#fff"/></svg>
    </div>
  </div>
</section>

<footer class="abs footer" role="img" aria-label="Dunkelblauer Hintergrund mit Molekülstrukturen">
  <h3 class="display" style="left:89px">Kontakt Details</h3>
  <div class="contact-line" style="top:92px">
    <svg width="12" height="16" viewBox="0 0 12 16"><path d="M6 0a6 6 0 0 0-6 6c0 4 6 10 6 10s6-6 6-10a6 6 0 0 0-6-6zm0 8.5a2.5 2.5 0 1 1 0-5 2.5 2.5 0 0 1 0 5z" fill="#e3202b"/></svg>
    <span>Address:</span><span>123 Street Name, City Name<br>Country Name</span>
  </div>
  <div class="contact-line" style="top:150px">
    <svg width="14" height="14" viewBox="0 0 14 14"><path d="M3 0l3 3-2 2c1 2 3 4 5 5l2-2 3 3-2 3C6 14 0 8 0 2z" fill="#e3202b"/></svg>
    <span>Phone:</span><span>+123 456 789</span>
  </div>
  <div class="contact-line" style="top:190px">
    <svg width="16" height="12" viewBox="0 0 16 12"><rect width="16" height="12" fill="#e3202b"/><path d="M0 0l8 6 8-6" stroke="#123454" stroke-width="1.3" fill="none"/></svg>
    <span>E-mail:</span><span>info@velunora.com</span>
  </div>

  <h3 class="display" style="left:543px;top:42px">Schnelle Links</h3>
  <ul class="links">
    <li>Home</li><li>Philosophie</li><li>Diagnose</li><li>Therapie</li><li>Kontakt</li><li>Über uns</li>
  </ul>

  <h3 class="display" style="left:930px">Folge Uns</h3>
  <div class="social"><span></span><span></span><span></span></div>
  <div class="brand">
    <span class="brand-mark"></span>
    <span class="brand-name">VELUNORA</span>
  </div>
</footer>

<div class="abs copyright">© Copyright 2018 <span>Velunora.de</span> . All rights reserved.</div>

</body>
</html>
```